Roofing Business needs a modern trade show booth design

Our booth is going to be a 10x10 area. we would like a back drop with two roll up banner on the sides. we would also like to have a rectangle table with our design on it.like this one https://www.flagmorrow.ca/fabric-pop-up-booth-square/p
our website is www.ridgevalebuilds.ca we are updating our logo. the new one is attached. We would like one of the banners to have a vacation give away I have attached examples. Our Main Focus is roofing and eavestrough.

Target Market(s)

Home owners.

Colors

Designer to choose colors to be used in the design.

Requirements
Must have
• The same colours as my logo

```html
<!DOCTYPE html>
<html lang="en">
<head>
<meta charset="utf-8">
<title>Ridgevale Roofing &amp; Exteriors – Trade Booth Set</title>
<link href="https://fonts.googleapis.com/css2?family=Anton&family=Montserrat:wght@400;600;700;800;900&family=Libre+Baskerville:wght@700&display=swap" rel="stylesheet">
<style>
  :root {
    --orange: #f29f1e;
    --orange-deep: #d98200;
    --navy: #0d2234;
    --navy-deep: #021e30;
    --sky: #3faaea;
    --sky-light: #5cbcf0;
    --slate: #5d6066;
    --paper: #efefef;
    --white: #ffffff;
    --label: #f4f4f4;
  }
  * { box-sizing: border-box; margin: 0; padding: 0; }
  html, body { width: 1200px; height: 1161px; overflow: hidden; }
  body {
    position: relative;
    font-family: "Montserrat", Arial, sans-serif;
    background: linear-gradient(135deg, #3c3c3c 0%, #555 50%, #6b6b6b 100%);
    color: var(--white);
  }
  .piece-label {
    position: absolute;
    font-weight: 400;
    font-size: 27px;
    color: var(--label);
    text-align: center;
    letter-spacing: -0.3px;
  }
  .panel { position: absolute; overflow: hidden; box-shadow: 0 6px 14px rgba(0,0,0,.35); }
  .abs { position: absolute; }
  .center-x { left: 0; right: 0; text-align: center; }

  .brand-name {
    font-family: "Montserrat", Arial, sans-serif;
    font-weight: 800;
    text-transform: uppercase;
    line-height: 1;
    text-align: center;
  }
  .brand-name .line-main { display: block; }
  .brand-name .line-sub { display: block; letter-spacing: 3px; }

  /* ---------- Backdrop ---------- */
  .backdrop { left: 293px; top: 102px; width: 618px; height: 616px; background: var(--navy); }
  .backdrop-header {
    left: 0; top: 0; width: 618px; height: 148px;
    background: linear-gradient(120deg, #e4e4e4 0%, #f5f5f5 45%, #e2e2e2 100%);
  }
  .backdrop-header .brand-name { position: absolute; left: 0; right: 0; top: 50px; color: var(--slate); }
  .backdrop-header .line-main { font-size: 40px; letter-spacing: 1px; }
  .backdrop-header .line-sub { font-size: 11px; margin-top: 8px; letter-spacing: 4px; }
  .backdrop-house {
    left: 0; top: 148px; width: 618px; height: 310px;
    background: linear-gradient(180deg, #0f2030 0%, #3a3027 40%, #7a4e36 75%, #2a2420 100%);
  }
  .backdrop-headline {
    top: 172px;
    font-family: "Anton", Impact, sans-serif;
    font-size: 54px;
    line-height: 1;
    color: #ececec;
    letter-spacing: 0.5px;
  }
  .service-strip {
    left: 74px; top: 237px; width: 467px; height: 31px;
    background: var(--orange);
    font-weight: 700; font-size: 16px; line-height: 31px;
    text-align: center; color: var(--white);
  }
  .project-photo { top: 294px; width: 147px; height: 117px; }
  .project-photo::after {
    content: ""; position: absolute; inset: 5px;
    border: 1px solid var(--orange);
  }
  .photo-roof { left: 76px; background: linear-gradient(180deg, #a8b7c4 0%, #6b6d6e 50%, #3e4248 100%); }
  .photo-crew { left: 235px; background: linear-gradient(180deg, #c6d6e6 0%, #9c5a3a 55%, #c98f68 100%); }
  .photo-siding { left: 392px; background: linear-gradient(150deg, #9aa8c4 0%, #6c5a4c 45%, #d9c190 100%); }
  .backdrop-footer {
    left: 0; top: 458px; width: 618px; height: 158px;
    background: linear-gradient(180deg, var(--orange-deep) 0%, #d57f00 100%);
  }
  .estimate-tag {
    left: 102px; top: 435px; width: 412px; height: 47px;
    background: var(--white);
    clip-path: polygon(4% 0, 100% 0, 96% 100%, 0 100%);
    color: var(--navy);
    font-weight: 800; font-size: 32px; line-height: 47px; text-align: center;
  }
  .backdrop-phone {
    top: 490px; font-weight: 700; font-size: 41px; line-height: 1.1;
    display: flex; justify-content: center; align-items: center; gap: 12px;
  }
  .backdrop-phone svg { width: 34px; height: 34px; }
  .backdrop-web { top: 540px; font-size: 19px; font-weight: 600; letter-spacing: 5px; }

  /* ---------- Left rollup ---------- */
  .rollup-services { left: 57px; top: 247px; width: 201px; height: 471px; background: var(--paper); }
  .rollup-services .sky {
    left: 0; top: 0; width: 201px; height: 100px;
    background: linear-gradient(180deg, var(--sky) 0%, var(--sky-light) 100%);
  }
  .rollup-services .brand-name { position: absolute; left: 0; right: 0; top: 66px; color: var(--white); font-weight: 800; }
  .rollup-services .brand-name .line-main { font-size: 22px; }
  .rollup-services .brand-name .line-sub { font-size: 6.5px; margin-top: 3px; letter-spacing: 2px; }
  .home-photo {
    left: 0; top: 100px; width: 201px; height: 94px;
    background: linear-gradient(180deg, #6c86a4 0%, #4c5564 45%, #5c7a48 100%);
  }
  .services-tab {
    left: 0; top: 180px; width: 150px; height: 27px;
    background: var(--orange);
    clip-path: polygon(0 0, 90% 0, 100% 100%, 0 100%);
    font-weight: 800; font-size: 16px; line-height: 27px; padding-left: 26px;
  }
  .service-list { left: 27px; top: 216px; width: 170px; list-style: none; color: var(--navy); }
  .service-list li {
    position: relative; padding-left: 13px;
    font-weight: 700; font-size: 12px; line-height: 15px; margin-bottom: 6px;
  }
  .service-list li::before {
    content: "»"; position: absolute; left: 0; top: -1px; color: var(--orange); font-weight: 800;
  }
  .rollup-services .footer {
    left: 0; top: 382px; width: 201px; height: 89px;
    background: var(--orange-deep);
  }
  .rollup-services .estimate-bar {
    left: 19px; top: 372px; width: 160px; height: 19px;
    background: var(--navy);
    clip-path: polygon(5% 0, 100% 0, 95% 100%, 0 100%);
    font-weight: 700; font-size: 11px; line-height: 19px; text-align: center;
  }
  .rollup-phone {
    top: 398px; font-weight: 700; font-size: 19px;
    display: flex; justify-content: center; align-items: center; gap: 5px;
  }
  .rollup-phone svg { width: 16px; height: 16px; }
  .rollup-web { top: 428px; font-size: 10px; font-weight: 600; }

  /* ---------- Right rollup ---------- */
  .rollup-giveaway { left: 947px; top: 248px; width: 199px; height: 468px; background: var(--navy-deep); }
  .travel-photo {
    left: 0; top: 0; width: 199px; height: 314px;
    background: linear-gradient(180deg, #3ea9ea 0%, #6cc3ef 30%, #2e8fa6 55%, #7a6a5c 85%, #a49a8c 100%);
  }
  .giveaway-head {
    top: 22px; font-weight: 900; font-size: 22px; line-height: 24px;
    color: var(--white); text-align: center;
  }
  .appointment-box {
    left: 18px; top: 73px; width: 163px; height: 33px;
    background: var(--orange);
    font-family: "Anton", Impact, sans-serif; font-size: 27px; line-height: 33px; text-align: center;
  }
  .giveaway-today { top: 106px; font-weight: 900; font-size: 33px; line-height: 36px; }
  .vacation-band {
    left: 0; top: 314px; width: 199px; height: 66px;
    background: var(--orange-deep);
    font-family: "Libre Baskerville", Georgia, serif;
    font-size: 22px; line-height: 22px; letter-spacing: 2px; text-align: center;
    padding-top: 12px;
  }
  .giveaway-phone {
    top: 393px; font-weight: 700; font-size: 20px;
    display: flex; justify-content: center; align-items: center; gap: 5px;
  }
  .giveaway-phone svg { width: 16px; height: 16px; }
  .giveaway-web { top: 422px; font-size: 10.5px; font-weight: 600; }

  /* ---------- Counter ---------- */
  .counter { left: 348px; top: 843px; width: 516px; height: 266px; background: var(--navy-deep); }
  .counter .brand-name { position: absolute; left: 0; right: 0; top: 118px; color: var(--white); }
  .counter .line-main { font-size: 35px; letter-spacing: 1px; }
  .counter .line-sub { font-size: 11px; margin-top: 8px; letter-spacing: 4px; }
  .counter-web {
    left: 147px; top: 208px; width: 223px; height: 24px;
    background: var(--orange-deep);
    font-weight: 600; font-size: 11px; line-height: 24px; text-align: center;
  }
</style>
</head>
<body>

<svg width="0" height="0" style="position:absolute">
  <defs>
    <symbol id="icon-phone" viewBox="0 0 24 24">
      <circle cx="12" cy="12" r="10.5" fill="none" stroke="currentColor" stroke-width="1.8"/>
      <path d="M8.6 6.6l1.7 -.3 1.1 2.6-1.2 1c.6 1.4 1.6 2.5 3 3.1l1-1.2 2.6 1.1-.3 1.7c-.2.6-.8 1-1.5.9-3.8-.6-6.8-3.6-7.3-7.4-.1-.7.3-1.3.9-1.5z" fill="currentColor"/>
    </symbol>
  </defs>
</svg>

<div class="piece-label" style="left:293px;width:618px;top:44px;">10*10 TRADEBOOTH</div>
<div class="piece-label" style="left:57px;width:201px;top:172px;">ROLLUP</div>
<div class="piece-label" style="left:947px;width:199px;top:172px;">ROLLUP</div>
<div class="piece-label" style="left:348px;width:516px;top:788px;">BOOTH COUNTER TABLE</div>

<!-- Backdrop -->
<section class="panel backdrop">
  <div class="abs backdrop-header">
    <div class="brand-name"><span class="line-main">Ridgevale</span><span class="line-sub">Roofing &amp; Exteriors</span></div>
  </div>
  <div class="abs backdrop-house" role="img" aria-label="Photo of a house with a terracotta tile roof at dusk"></div>
  <h1 class="abs center-x backdrop-headline">ROOFING DONE RIGHT</h1>
  <div class="abs service-strip">Roofing • Siding • Windows &amp; Doors • Eavestroughs</div>
  <div class="abs project-photo photo-roof" role="img" aria-label="Photo of a grey shingle roof among pine trees"></div>
  <div class="abs project-photo photo-crew" role="img" aria-label="Photo of roofers working on a new roof"></div>
  <div class="abs project-photo photo-siding" role="img" aria-label="Photo of a house gable with beige siding"></div>
  <div class="abs backdrop-footer"></div>
  <div class="abs estimate-tag">GET FREE ESTIMATE</div>
  <div class="abs center-x backdrop-phone"><svg><use href="#icon-phone"/></svg>877-555-0148</div>
  <div class="abs center-x backdrop-web">www.ridgevalebuilds.ca</div>
</section>

<!-- Services rollup -->
<section class="panel rollup-services">
  <div class="abs sky"></div>
  <div class="abs home-photo" role="img" aria-label="Photo of a row of suburban houses"></div>
  <div class="brand-name" style="top:22px"><span class="line-main">Ridgevale</span><span class="line-sub">Roofing &amp; Exteriors</span></div>
  <div class="abs services-tab">SERVICES</div>
  <ul class="abs service-list">
    <li>Roofing Services</li>
    <li>Roof Eavestrough Services</li>
    <li>Windows &amp; Doors</li>
    <li>Siding Repairs &amp; Installation</li>
    <li>Wood Siding</li>
    <li>Fiber Cement Siding</li>
  </ul>
  <div class="abs footer"></div>
  <div class="abs estimate-bar">GET FREE ESTIMATE</div>
  <div class="abs center-x rollup-phone"><svg><use href="#icon-phone"/></svg>877-555-0148</div>
  <div class="abs center-x rollup-web">www.ridgevalebuilds.ca</div>
</section>

<!-- Giveaway rollup -->
<section class="panel rollup-giveaway">
  <div class="abs travel-photo" role="img" aria-label="Photo of a traveller in a sun hat on a boat bow near tropical islands"></div>
  <div class="abs center-x giveaway-head">BOOK YOUR<br>REMODEL</div>
  <div class="abs appointment-box">APPOINTMENT</div>
  <div class="abs center-x giveaway-today">TODAY</div>
  <div class="abs vacation-band">VACATION<br>TOMORROW</div>
  <div class="abs center-x giveaway-phone"><svg><use href="#icon-phone"/></svg>877-555-0148</div>
  <div class="abs center-x giveaway-web">www.ridgevalebuilds.ca</div>
</section>

<!-- Counter table -->
<section class="panel counter">
  <div class="brand-name"><span class="line-main">Ridgevale</span><span class="line-sub">Roofing &amp; Exteriors</span></div>
  <div class="abs counter-web">www.ridgevalebuilds.ca</div>
</section>

</body>
</html>
```